DESSERT FLYER

We need a flyer design for desserts and drinks for our restaurant.

We use Retro/rustic as main theme

Flyer must include all images, which are attached to this project. We also named correctly for each images, so you can use for each dish's title (docx file)
Must include our logo as well.

Flyer tittle is "SWEET PLUMO"

Please see our website for reference at brickhollow.com.au

Flyer's printing size is A5 Vertical. Single Side

```html
<!DOCTYPE html>
<html lang="en">
<head>
<meta charset="utf-8">
<title>Sweet Plumo – Dessert Flyer</title>
<link href="https://fonts.googleapis.com/css2?family=Paytone+One&family=Stardos+Stencil:wght@700&family=Josefin+Sans:wght@700&display=swap" rel="stylesheet">
<style>
  :root{
    --canvas:#ffffff;
    --plank-teal:#3fb0aa;
    --plank-teal-dark:#2f9892;
    --plank-white:#ebe8e2;
    --plank-line:#cfcac1;
    --post-brown:#8a4a22;
    --panel-brown:#7b3f1e;
    --banner-dark:#2f2522;
    --accent-orange:#e48a5e;
    --logo-teal:#1a8b95;
    --logo-teal-light:#5cc3c9;
    --caption:#ffffff;
    --mint:#4fa83a;
  }
  *{margin:0;padding:0;box-sizing:border-box}
  html,body{width:1200px;height:1000px;overflow:hidden;background:var(--canvas)}
  .canvas{position:relative;width:1200px;height:1000px}
  .flyer{position:absolute;left:262px;top:18px;width:676px;height:962px;overflow:hidden;
    background:repeating-linear-gradient(180deg,var(--plank-white) 0 50px,var(--plank-line) 50px 52px)}
  .planks-teal{position:absolute;left:0;top:0;width:676px;height:335px;
    background:repeating-linear-gradient(180deg,var(--plank-teal) 0 66px,var(--plank-teal-dark) 66px 69px)}
  .planks-teal.bottom{top:878px;height:84px}
  .post{position:absolute;top:2px;width:63px;height:205px;background:var(--post-brown)}
  .post.left{left:33px}.post.right{left:580px}
  .signboard{position:absolute;left:96px;top:2px;width:484px;height:270px;
    background:repeating-linear-gradient(180deg,#f1efea 0 44px,#dcd8d0 44px 46px)}
  .brand{position:absolute;left:0;width:100%;text-align:center;font-family:"Josefin Sans",sans-serif;white-space:nowrap}
  .brand-name{top:100px;font-family:"Paytone One",sans-serif;font-size:38px;line-height:1;color:var(--logo-teal);letter-spacing:1px}
  .brand-place{top:186px;font-size:12px;color:var(--accent-orange);letter-spacing:2px}
  .brand-est{top:210px;font-size:12px;color:var(--logo-teal-light);letter-spacing:2px}
  .mint{position:absolute;background:var(--mint);border-radius:50%}
  .mint.one{left:0;top:2px;width:140px;height:165px;border-radius:45% 55% 50% 40%}
  .mint.two{left:510px;top:205px;width:125px;height:105px}
  .title-banner{position:absolute;left:-8px;top:268px;width:392px;height:96px;background:var(--banner-dark);
    transform:rotate(-5deg);transform-origin:left top;display:flex;align-items:center;padding-left:24px}
  .title{font-family:"Stardos Stencil",serif;font-weight:700;font-size:44px;line-height:1;color:var(--accent-orange);letter-spacing:1px;white-space:nowrap}
  .menu-board{position:absolute;left:30px;top:350px;width:616px;height:612px;background:var(--panel-brown);
    display:grid;grid-template-columns:1fr 1fr;grid-template-rows:204px 206px 202px}
  .dish{position:relative;border:1px solid #5e2f16;padding:4px 12px 0 12px}
  .dish-photo{width:282px;height:164px;border-radius:12px}
  .dish-caption{position:absolute;right:14px;bottom:4px;text-align:right;color:var(--caption);
    font-family:"Paytone One",sans-serif;font-size:9.5px;line-height:1.15;letter-spacing:.4px}
  .dish-price{display:block;font-family:Arial,sans-serif;font-size:10px}
</style>
</head>
<body>
<div class="canvas">
  <div class="flyer">
    <div class="planks-teal"></div>
    <div class="planks-teal bottom"></div>
    <div class="post left"></div>
    <div class="post right"></div>
    <div class="signboard">
      <div class="brand brand-name">BRICK HOLLOW</div>
      <div class="brand brand-place">EASTVALE</div>
      <div class="brand brand-est">EST. 2014</div>
    </div>
    <div class="mint one" role="img" aria-label="Fresh mint leaves"></div>
    <div class="mint two" role="img" aria-label="Sprig of mint leaves"></div>
    <div class="title-banner"><h1 class="title">SWEET PLUMO</h1></div>

    <section class="menu-board">
      <article class="dish">
        <div class="dish-photo" role="img" aria-label="Banana fritters on a banana leaf" style="background:radial-gradient(circle at 40% 45%,#e7a04d,#c77a2c 55%,#4f8a2e)"></div>
        <p class="dish-caption">BANANA FRITTER WITH VANILLA ICE CREAM<span class="dish-price">$6.90</span></p>
      </article>
      <article class="dish">
        <div class="dish-photo" role="img" aria-label="Banana sago pudding on a banana leaf" style="background:radial-gradient(ellipse at 50% 45%,#f6f7f5 30%,#cfd8c8 45%,#3e8a2f 70%)"></div>
        <p class="dish-caption">BANANA SAGO PUDDING WITH PEANUT TOPPING<span class="dish-price">$6.90</span></p>
      </article>
      <article class="dish">
        <div class="dish-photo" role="img" aria-label="Black sticky rice with mango" style="background:linear-gradient(120deg,#3d2340 0 45%,#f2d54a 60%,#e9c13a)"></div>
        <p class="dish-caption">BLACK STICKY RICE WITH MANGO<span class="dish-price">$6.90</span></p>
      </article>
      <article class="dish">
        <div class="dish-photo" role="img" aria-label="Fried ice cream in a glass bowl" style="background:radial-gradient(circle at 55% 55%,#f2efe6,#e09a52 35%,#8e9a93 60%,#3c4d46)"></div>
        <p class="dish-caption">FRIED ICE CREAM WITH CARAMEL CHOCOLATE<br>STRAWBERRY TOPPING<span class="dish-price">$6.90</span></p>
      </article>
      <article class="dish">
        <div class="dish-photo" role="img" aria-label="Vietnamese drip coffee being poured" style="background:linear-gradient(135deg,#a08a72,#6b5746 55%,#3a2d24)"></div>
        <p class="dish-caption">VIETNAMESE COFFEE<span class="dish-price">$6.90</span></p>
      </article>
      <article class="dish">
        <div class="dish-photo" role="img" aria-label="Fresh young coconut drink on a table" style="background:linear-gradient(160deg,#8a3c28,#b5653b 45%,#efe6d2 75%)"></div>
        <p class="dish-caption">FRESH YOUNG COCONUT JUICE<span class="dish-price">$5.50</span></p>
      </article>
    </section>
  </div>
</div>
</body>
</html>
```